Brochure, website and corporate stationary Design Project

Project scope:
1 x brochure (A4 insert) design
1 x brochure folder design (both external pages and one internal (there will be a few lines of text on the left inside page). The internal right side page will be a pocket for brochures (A4 inserts)
1 x corporate stationary pack (Business Card, logo (a proper logo file format needs to be produced), Letterhead and Envelope)
1 x concept design for our website. You dont need to do the coding. What you need to deliver is the design in a standard format (i.e. photoshop or blend)
Summary: the scope of the project is to design our brochure and its brochure folder, corporate stationary design and graphics concept design for our website. You should also consider our existing logo when performing the above design work (you can modify the logo slightly if you think it would improve look and feel and relevancy to overall design).
• We are a small IT services company
• The folder will be used to hold the brochures (inserts). The folder will be given to prospect customers (see attached a sample service brochure called “VelmaroX User support services Ver0.1.docx”)
• On the cover of the folder, we want to have a design that uses keywords / phrases that reflects our main services (see attached file called “Phrases for presentation folder.docs”). Please note that not all phrases have to be used, use a logic in which ones or add new suggestions
• Inside the folder, at left side we want to have a short text explaining about our services a bit (see attached file called “Brochure Main section v0.91.docx”)
• All designs (corporate stationary, brochure, folder, web, etc.) must be consistent with each other and follow same concept, colour scheme, etc
• you are allowed to do minor changes to our existing logo if you have good reason to do so (see attached logo)
• We want our website design to be simple, elegant, not very colourful, light. HTML5. No flash. (you dont need to do the actual coding of the website, just deliver the design in Photoshop, Blend or any other standard format) With minimal menu items such as: home, services, about us, news, contact us, and other important ones if any. Same colour and design scheme as corporate stationary and brochures
• The company name “VelmaroX” is derived from the Swedish word “Grön” (meaning green) and “roX” which stands for technology but spelled with a “Q” to resemble Quality. The corporate green colour comes from the word “Grön”.
• All templates must be delivered in a standard editable format
Reason: To provide more time to the designers to come with their design submissions.
please note that we more than doubled the budget for this project
Target Market(s)
We deliver IT services to companies of 3-4 employees upto 200-300 employees. The brochures are intended for prospect customers (non IT people)
Industry/Entity Type
Business
Look and feel

```html
<!DOCTYPE html>
<html lang="en">
<head>
<meta charset="utf-8">
<title>VelmaroX – Presentation Folder</title>
<link rel="stylesheet" href="https://fonts.googleapis.com/css2?family=Open+Sans:wdth,wght@75..100,300..800&display=swap">
<style>
  :root {
    --paper: #ffffff;
    --folder-green: #356150;
    --flap-green: #33604d;
    --edge-green: #4c8a5c;
    --accent-green: #7cb55a;
    --text-white: #ffffff;
    --text-soft: #d6e2da;
  }
  html, body {
    margin: 0;
    padding: 0;
    overflow: hidden;
    background: var(--paper);
  }
  .canvas {
    position: relative;
    width: 1200px;
    height: 917px;
    overflow: hidden;
    background: var(--paper);
    font-family: "Open Sans", Arial, sans-serif;
  }
  .flaps {
    position: absolute;
    left: 0;
    top: 0;
  }
  .cover {
    position: absolute;
    left: 179px;
    top: 19px;
    width: 997px;
    height: 686px;
    background:
      linear-gradient(90deg, var(--edge-green) 0%, var(--folder-green) 22%, var(--folder-green) 76%, var(--edge-green) 100%);
  }
  .accent-bar {
    position: absolute;
    left: 645px;
    top: 362px;
    width: 31px;
    height: 343px;
    background: var(--accent-green);
  }
  .headline {
    position: absolute;
    left: 709px;
    top: 254px;
    margin: 0;
    font-size: 27px;
    line-height: 26px;
    font-weight: 700;
    font-stretch: 75%;
    color: var(--text-white);
  }
  .services {
    position: absolute;
    left: 709px;
    top: 358px;
    margin: 0;
    padding: 0;
    list-style: none;
    font-size: 13.5px;
    line-height: 14.1px;
    font-weight: 300;
    color: var(--text-soft);
  }
  .brand {
    position: absolute;
    right: 586px;
    top: 432px;
    margin: 0;
    font-size: 36px;
    font-weight: 700;
    color: var(--text-white);
    letter-spacing: 0.5px;
  }
  .contact {
    position: absolute;
    right: 586px;
    top: 503px;
    margin: 0;
    text-align: right;
    font-size: 13px;
    line-height: 14px;
    color: var(--text-soft);
    font-weight: 300;
  }
  .contact dt {
    font-weight: 700;
    font-stretch: 75%;
    color: var(--text-white);
    font-size: 13.5px;
  }
  .contact dd { margin: 0; }
  .contact .group-gap { margin-top: 14px; }
</style>
</head>
<body>
<main class="canvas">
  <svg class="flaps" width="1200" height="917" viewBox="0 0 1200 917" aria-hidden="true">
    <path class="side-flap" fill="var(--flap-green)"
      d="M179 198 L150 198 Q112 200 104 250 L21 651 L179 706 Z"/>
    <path class="bottom-flap" fill="var(--flap-green)"
      d="M179 705 L666 705 L666 794 Q520 880 310 896 L278 850 Q270 870 250 862 Q205 840 200 795 Q202 765 225 770 L179 705 Z"/>
  </svg>

  <section class="cover">
  </section>

  <div class="accent-bar"></div>

  <h1 class="headline">Grow your<br>business with us!</h1>

  <ul class="services">
    <li>IT support</li>
    <li>IT Service level agreement</li>
    <li>IT Helpdesk services</li>
    <li>IT security</li>
    <li>IT infrastructure</li>
    <li>Network</li>
    <li>Cloud services</li>
    <li>Hosted email</li>
    <li>Hosted mail server</li>
    <li>Application hosting</li>
    <li>Cloud email</li>
    <li>Mail clients</li>
    <li>Office suites</li>
    <li>Web development</li>
    <li>Business Process Management</li>
    <li>IT Management consultancy</li>
    <li>Business applications</li>
    <li>ERP</li>
    <li>CRM</li>
    <li>Accounting software</li>
    <li>SEO</li>
    <li>Search engine optimization</li>
  </ul>

  <p class="brand">VelmaroX</p>

  <dl class="contact">
    <dt>Visit Address</dt>
    <dd>Block 7, 3rd Floor</dd>
    <dd>Harbour Tech Park, Solmere</dd>
    <dt class="group-gap">Mail Address</dt>
    <dd>PO BOX: 410 316</dd>
    <dd>Harbour Tech Park, Solmere</dd>
    <dt class="group-gap">Phone</dt>
    <dd>+000 55 2043186</dd>
    <dt>Fax</dt>
    <dd>+000 4 318 6620</dd>
  </dl>
</main>
</body>
</html>
```